Need Business Cards for my Business

email address: rkpmarlowhollowworks@vendrimail.com
web address: rkpmarlowhollowworks.net
Slogan: We offer various QVN licenses
Rowland K. Pemberly
Please stick with colors of Company Logo
would like the card to be more of the color example of the logo.
If you need PDF copy of logo email me at the above account.
Creative control rests with you.

Industry/Entity Type

Business

Contact Information for Business Card

I am a minimalist, but would like something to pop and stand out amongst other cards, make it memorable.

Font styles to use
Serif
Decorative
Script

```html
<!DOCTYPE html>
<html lang="en">
<head>
<meta charset="utf-8">
<title>Marlow Hollow Works – Business Card</title>
<link href="https://fonts.googleapis.com/css2?family=Roboto+Condensed:ital,wght@0,400;0,700;1,400&display=swap" rel="stylesheet">
<style>
  :root {
    --backdrop: #56473a;
    --card-light: #ffffff;
    --card-dark: #231f20;
    --ink: #231f20;
    --ink-soft: #5b5b5b;
    --paper-white: #ffffff;
    --slogan-grey: #8d8d8d;
  }
  * { margin: 0; padding: 0; box-sizing: border-box; }
  html, body { width: 1200px; height: 987px; overflow: hidden; }
  body {
    background: var(--backdrop);
    font-family: "Roboto Condensed", sans-serif;
    position: relative;
  }
  .card {
    position: absolute;
    left: 293px;
    width: 615px;
    height: 351px;
    box-shadow: 0 2px 6px rgba(0,0,0,0.35);
    overflow: hidden;
  }
  .card--front { top: 122px; background: var(--card-light); }
  .card--back { top: 513px; background: var(--card-dark); }

  .brand-mark {
    position: absolute;
    left: 22px;
    top: 110px;
    font-size: 120px;
    font-weight: 700;
    line-height: 1;
    color: var(--ink);
    letter-spacing: 2px;
  }
  .edge-tab { position: absolute; right: 0; top: 54px; }

  .contact {
    position: absolute;
    right: 30px;
    top: 46px;
    text-align: right;
    color: var(--ink-soft);
    font-size: 15px;
    line-height: 21px;
  }
  .contact__name {
    font-size: 21px;
    font-weight: 700;
    color: var(--ink);
    line-height: 26px;
  }
  .contact__role { margin-bottom: 9px; }
  .contact__lines { margin-bottom: 8px; }

  .back-brand {
    position: absolute;
    left: 0; right: 0;
    top: 140px;
    display: flex;
    align-items: center;
    justify-content: center;
    gap: 14px;
    color: var(--paper-white);
    font-size: 34px;
    font-weight: 700;
    letter-spacing: 1px;
    text-transform: uppercase;
  }
  .back-brand__dot {
    width: 22px; height: 22px;
    border-radius: 50%;
    background: var(--paper-white);
  }
  .slogan {
    position: absolute;
    left: 0; right: 0;
    top: 296px;
    display: flex;
    align-items: center;
    justify-content: center;
    gap: 6px;
    color: var(--slogan-grey);
    font-size: 15px;
    font-style: italic;
    text-transform: uppercase;
    letter-spacing: 0.5px;
  }
  .slogan__rule {
    width: 70px; height: 1px;
    background: linear-gradient(90deg, rgba(141,141,141,0), var(--slogan-grey));
  }
  .slogan__rule--right {
    background: linear-gradient(90deg, var(--slogan-grey), rgba(141,141,141,0));
  }
</style>
</head>
<body>
  <section class="card card--front">
    <div class="brand-mark">RKP</div>
    <svg class="edge-tab" width="10" height="48" viewBox="0 0 10 48" aria-hidden="true">
      <polygon points="0,0 10,0 10,48 0,36" fill="var(--ink)"/>
    </svg>
    <div class="contact">
      <p class="contact__name">Rowland K. Pemberly</p>
      <p class="contact__role">CEO/Founder</p>
      <div class="contact__lines">
        <p>Phone : 301-555-0148</p>
        <p>Mobile : 836 555 0172</p>
        <p>rkpmarlowhollowworks@vendrimail.com</p>
        <p>rkpmarlowhollowworks.net</p>
      </div>
      <ul class="contact__licenses" style="list-style:none">
        <li>General Radiotelephone Operator License</li>
        <li>Marine Radio Operator License Permit</li>
        <li>GMDSS Radio Operators License</li>
        <li>GMDSS Radio Maintainers License</li>
        <li>Ship Radar Endorsement</li>
      </ul>
    </div>
  </section>

  <section class="card card--back">
    <div class="back-brand">
      <span class="back-brand__dot"></span>
      <span>Marlow Hollow Works</span>
    </div>
    <div class="slogan">
      <span class="slogan__rule"></span>
      <span>We offer various QVN licenses</span>
      <span class="slogan__rule slogan__rule--right"></span>
    </div>
  </section>
</body>
</html>
```